Verimont Designs business card

Front of card should be logo and back of card should be communication info.
Please note: reverse the logo color. Card should be black and everything else white.

Industry/Entity Type

Custom home design/construction

Contact Information for Business Card

Verimont Designs, LLC 614-382-9017 verimontdesigns@quillmail.example

Requirements
Must have
• Square card, Logo on front, communication info on back and perhaps a mini version of the logo on back also. Black card/white lettering. Double sides square card.
Nice to have
• I want to keep it simple. Our product (custom homes) speak for themselves.

```html
<!DOCTYPE html>
<html lang="en">
<head>
<meta charset="utf-8">
<title>Verimont Designs business card</title>
<link rel="stylesheet" href="https://fonts.googleapis.com/css2?family=Poppins:wght@400;500;600&display=swap">
<style>
  :root {
    --backdrop: #dadada;
    --card: #1a1a1a;
    --ink: #ffffff;
    --rule: #8a8a8a;
    --deboss: #2c2c2c;
  }
  * { margin: 0; padding: 0; box-sizing: border-box; }
  html, body { width: 1200px; height: 900px; overflow: hidden; }
  body {
    background: var(--backdrop);
    position: relative;
    font-family: "Poppins", sans-serif;
    color: var(--ink);
  }
  .card {
    position: absolute;
    top: 256px;
    width: 398px;
    height: 398px;
    background: var(--card);
  }
  .card--info { left: 205px; }
  .card--brand { left: 653px; }

  .wordmark {
    position: absolute;
    text-align: right;
    line-height: 1;
    text-transform: uppercase;
    font-weight: 500;
  }
  .card--info .wordmark { right: 26px; top: 147px; }
  .wordmark__name { font-size: 21px; letter-spacing: 0.5px; }
  .wordmark__tagline { font-size: 14.5px; letter-spacing: 1.4px; margin-top: 5px; }

  .card--brand .wordmark {
    left: 0; right: 0; top: 234px;
    text-align: center;
    color: var(--deboss);
  }
  .card--brand .wordmark__name { font-size: 28px; letter-spacing: 1px; }
  .card--brand .wordmark__tagline { font-size: 18px; letter-spacing: 2px; margin-top: 4px; }

  .person { position: absolute; left: 30px; top: 247px; line-height: 1.2; }
  .person__name { font-size: 19px; font-weight: 600; letter-spacing: 0.4px; text-transform: uppercase; }
  .person__role { font-size: 17px; font-weight: 400; }

  .divider {
    position: absolute;
    left: 31px; top: 303px;
    width: 332px; height: 1px;
    background: var(--rule);
  }

  .contact { position: absolute; left: 30px; top: 322px; list-style: none; }
  .contact__item {
    display: flex; align-items: center; gap: 4px;
    font-size: 18px; line-height: 27px; font-weight: 400;
  }
  .contact__icon { width: 20px; height: 20px; flex: none; }
</style>
</head>
<body>
  <section class="card card--info" aria-label="Contact side">
    <div class="wordmark">
      <div class="wordmark__name">Verimont Designs</div>
      <div class="wordmark__tagline">Custom Home Builders</div>
    </div>

    <div class="person">
      <div class="person__name">Daniel Hargrove</div>
      <div class="person__role">Managing Director</div>
    </div>

    <div class="divider"></div>

    <ul class="contact">
      <li class="contact__item">
        <svg class="contact__icon" viewBox="0 0 24 24" fill="none" stroke="#fff" stroke-width="2" stroke-linejoin="round">
          <path d="M5 3h4l2 5-3 2a11 11 0 0 0 6 6l2-3 5 2v4a2 2 0 0 1-2 2A17 17 0 0 1 3 5a2 2 0 0 1 2-2z"/>
        </svg>
        <span>614-382-9017</span>
      </li>
      <li class="contact__item">
        <svg class="contact__icon" viewBox="0 0 24 24" fill="#fff">
          <path d="M3 6h18v12H3z"/>
          <path d="M3 6l9 7 9-7" fill="none" stroke="#1a1a1a" stroke-width="1.6"/>
        </svg>
        <span>verimontdesigns@quillmail.example</span>
      </li>
    </ul>
  </section>

  <section class="card card--brand" aria-label="Brand side">
    <div class="wordmark">
      <div class="wordmark__name">Verimont Designs</div>
      <div class="wordmark__tagline">Custom Home Builders</div>
    </div>
  </section>
</body>
</html>
```